Banner 34"x81"

This is for a Pull Up Banner
I am supplying a sample of my logo and some of my art work for you to incorporate into an upright banner.
Please business name:TessaLu OpenHorizon Psychotherapy
phone number: 416-938-1054 NOT THE ONE ON THE BUSINESS CARD

```html
<!DOCTYPE html>
<html lang="en">
<head>
<meta charset="utf-8">
<title>TessaLu OpenHorizon Psychotherapy – Pull Up Banner</title>
<link rel="stylesheet" href="https://fonts.googleapis.com/css2?family=Poppins:wght@400;700&family=Oswald:wght@400;500&display=swap">
<style>
  :root {
    --backdrop: #2228c0;
    --banner-navy: #203f8f;
    --gold: #f5e13a;
    --gold-light: #f6e04a;
    --gold-deep: #dcb91e;
    --white: #ffffff;
    --mark-blue: #1f5aa8;
  }
  * { margin: 0; padding: 0; box-sizing: border-box; }
  html, body { width: 1200px; height: 1050px; overflow: hidden; }
  body { background: var(--backdrop); position: relative; }

  .banner {
    position: absolute; left: 388px; top: 25px;
    width: 424px; height: 1000px;
    background: var(--banner-navy);
    overflow: hidden;
  }

  .foil-area {
    position: absolute;
    background: linear-gradient(135deg, var(--gold-deep) 0%, var(--gold-light) 100%);
  }
  .foil-area-top { right: 0; top: 0; width: 314px; height: 200px; }
  .foil-area-bottom { right: 0; bottom: 0; width: 193px; height: 110px; }

  .portrait {
    position: absolute; left: 57px; top: 134px;
    width: 166px; height: 243px;
    border: 5px solid var(--white);
    background: linear-gradient(180deg, #3a2620 0%, #1f4fb0 55%, #2a211e 100%);
  }

  .brand { position: absolute; left: 59px; top: 396px; width: 310px; }
  .brand-practice {
    font-family: "Poppins", sans-serif; font-weight: 400;
    font-size: 39px; line-height: 44px; color: var(--gold);
  }
  .brand-name {
    font-family: "Poppins", sans-serif; font-weight: 700;
    font-size: 58px; line-height: 58px; color: var(--gold);
    margin-top: -4px;
  }
  .brand-field {
    font-family: "Oswald", sans-serif; font-weight: 500;
    font-size: 22px; line-height: 26px; color: var(--gold);
    letter-spacing: 12.6px; margin-top: 8px;
  }

  .contacts { position: absolute; left: 60px; top: 563px; list-style: none; }
  .contact { display: flex; align-items: center; color: var(--white); }
  .contact-phone {
    font-family: "Poppins", sans-serif; font-weight: 700;
    font-size: 37px; line-height: 44px; margin-bottom: 6px;
  }
  .contact-line {
    font-family: "Oswald", sans-serif; font-weight: 400;
    font-size: 21px; line-height: 28px; margin-bottom: 12px;
  }
  .contact-icon { flex: none; margin-right: 10px; }
  .dot { width: 28px; height: 28px; border-radius: 50%; background: var(--white); }

  .practice-mark {
    position: absolute; left: 60px; top: 805px;
    display: flex; align-items: center;
  }
  .practice-mark-square { width: 80px; height: 80px; background: var(--mark-blue); margin-right: 16px; }
  .practice-mark-name {
    font-family: "Poppins", sans-serif; font-weight: 700;
    font-size: 38px; color: var(--white);
  }
</style>
</head>
<body>
  <main class="banner">
    <div class="foil-area foil-area-top" role="img" aria-label="Gold foil paint splash artwork"></div>

    <div class="portrait" role="img" aria-label="Portrait photo of the therapist seated on a dark leather sofa in a blue top"></div>

    <header class="brand">
      <p class="brand-practice">OpenHorizon</p>
      <h1 class="brand-name">TessaLu</h1>
      <p class="brand-field">PSYCHOTHERAPY</p>
    </header>

    <ul class="contacts">
      <li class="contact contact-phone">
        <svg class="contact-icon" width="24" height="38" viewBox="0 0 24 38" aria-hidden="true">
          <rect x="2" y="2" width="20" height="34" rx="3" fill="none" stroke="#fff" stroke-width="2.5"/>
          <line x1="2" y1="8" x2="22" y2="8" stroke="#fff" stroke-width="2"/>
          <line x1="2" y1="29" x2="22" y2="29" stroke="#fff" stroke-width="2"/>
          <circle cx="12" cy="32.5" r="1.6" fill="#fff"/>
          <path d="M8 13 L10 12 L11.5 15 L10 16 C10.5 18 12 20 13.5 21 L15 20 L17 22.5 L15.5 24 C11 23 8 18 8 13 Z" fill="#fff"/>
        </svg>
        <span>416-938-1054</span>
      </li>
      <li class="contact contact-line">
        <svg class="contact-icon" width="28" height="28" viewBox="0 0 28 28" aria-hidden="true">
          <circle cx="14" cy="14" r="14" fill="#fff"/>
          <rect x="7" y="9" width="14" height="10" fill="none" stroke="#203f8f" stroke-width="1.6"/>
          <polyline points="7,9 14,15 21,9" fill="none" stroke="#203f8f" stroke-width="1.6"/>
        </svg>
        <span>TessaOpenHorizon@mailbox.com</span>
      </li>
      <li class="contact contact-line">
        <span class="contact-icon dot"></span>
        <span>@TessaOpenHorizon</span>
      </li>
      <li class="contact contact-line">
        <span class="contact-icon dot"></span>
        <span>@TessaHorizon</span>
      </li>
    </ul>

    <div class="practice-mark">
      <span class="practice-mark-square"></span>
      <span class="practice-mark-name">TessaLu</span>
    </div>

    <div class="foil-area foil-area-bottom" role="img" aria-label="Gold foil paint splash artwork"></div>
  </main>
</body>
</html>
```